Amber Heron Fund Pitch Deck

This is a PowerPoint for use in investor presentations. The copy is written (although it may have small tweaks) and the designer will be responsible for creating a template and some graphical representations inside the presentation.

Note on the logo. Only the Amber Heron should be used, not the text.

```html
<!DOCTYPE html>
<html lang="en">
<head>
<meta charset="utf-8">
<title>Amber Heron Fund – Pitch Deck</title>
<link href="https://fonts.googleapis.com/css2?family=Didact+Gothic&family=Nunito:wght@700;800&display=swap" rel="stylesheet">
<style>
:root{
  --page:#ffffff;
  --slide-light:#f6f6f6;
  --navy:#1c3a78;
  --navy-deep:#142a5c;
  --slate-top:#5a6fa3;
  --slate-bottom:#1a1e2b;
  --accent:#6b8cc9;
  --ink:#3a3a3a;
  --muted:#9a9a9a;
  --white:#ffffff;
}
*{margin:0;padding:0;box-sizing:border-box}
html,body{width:1200px;height:2194px;overflow:hidden;background:var(--page)}
body{position:relative;font-family:"Didact Gothic",sans-serif;color:var(--ink)}
.slide{position:absolute;left:191px;width:818px;height:460px;overflow:hidden;background:var(--slide-light);box-shadow:10px 14px 28px rgba(0,0,0,.28)}
.slide--cover{top:94px}
.slide--contents{top:609px}
.slide--edge{top:1124px}
.slide--tech{top:1639px}
.abs{position:absolute}
.footer-note{position:absolute;top:430px;left:254px;font-size:9.5px;color:var(--muted);white-space:nowrap}
.page-no{position:absolute;top:430px;left:714px;font-size:9.5px;color:var(--muted)}
.brand-mark{position:absolute;top:428px;left:52px;font-size:11px;color:var(--accent);white-space:nowrap}

/* cover */
.cover-photo{position:absolute;inset:0;background:linear-gradient(180deg,#8eaee3 0%,#7a9bd4 35%,#5b7bb0 70%,#3e5f8e 100%)}
.cover-frame{position:absolute;left:77px;top:53px;width:321px;height:328px;border:3px solid rgba(255,255,255,.9)}
.cover-panel{position:absolute;left:86px;top:60px;width:305px;height:312px;background:linear-gradient(180deg,rgba(150,170,200,.25) 0%,rgba(120,145,190,.55) 45%,#6b8cc9 75%,#6b8cc9 100%);box-shadow:0 4px 14px rgba(0,0,0,.25)}
.cover-dot{position:absolute;left:118px;top:262px;width:14px;height:14px;background:var(--white)}
.cover-title{position:absolute;left:117px;top:303px;font-family:"Nunito",sans-serif;font-weight:800;font-size:20px;letter-spacing:1px;color:var(--white)}
.slide--cover .footer-note{left:266px;color:rgba(255,255,255,.9)}
.slide--cover .page-no{color:rgba(255,255,255,.35)}

/* contents */
.contents-side{position:absolute;left:0;top:0;width:293px;height:460px;background:linear-gradient(180deg,var(--slate-top) 0%,#34406a 40%,#222737 75%,var(--slate-bottom) 100%)}
.contents-heading{position:absolute;left:73px;top:196px;font-size:20px;line-height:25px;color:var(--white);letter-spacing:.5px}
.contents-heading strong{font-family:"Nunito",sans-serif;font-weight:800}
.contents-frame{position:absolute;left:265px;top:46px;width:77px;height:349px;border:2px solid var(--white);box-shadow:inset 0 0 0 1px rgba(0,0,0,.04)}
.contents-list{position:absolute;left:307px;top:68px;list-style:none}
.contents-list li{display:flex;height:31.7px;align-items:center;font-size:17px;color:#333}
.contents-list .num{width:50px}
.slide--contents .brand-mark{color:var(--accent)}

/* section slides */
.diagonal{position:absolute;inset:0;width:818px;height:460px}
.section-card{position:absolute;top:88px;width:334px;height:283px;background:linear-gradient(180deg,#f2f2f2 0%,#cfcfcf 35%,#b6bfcf 55%,#6b8cc9 78%,#6b8cc9 100%);box-shadow:-8px 10px 22px rgba(0,0,0,.35)}
.section-num{position:absolute;top:14px;font-family:"Nunito",sans-serif;font-weight:800;font-size:27px;color:var(--accent)}
.section-title{position:absolute;bottom:24px;font-family:"Nunito",sans-serif;font-weight:800;font-size:21px;color:var(--white)}
.slide--edge .section-card{left:52px}
.slide--edge .section-num{left:15px}
.slide--edge .section-title{right:32px}
.edge-copy{position:absolute;left:416px;top:85px;width:347px;font-size:14px;line-height:24.6px;color:var(--white);text-align:justify}
.edge-copy p+p{margin-top:24.6px}
.slide--edge .footer-note,.slide--edge .page-no{color:rgba(255,255,255,.75)}
.slide--tech .section-card{left:431px;box-shadow:-8px 10px 22px rgba(0,0,0,.3)}
.slide--tech .section-num{right:15px}
.slide--tech .section-title{left:40px}
.tech-copy{position:absolute;left:55px;top:92px;width:329px;font-size:13.4px;line-height:23px;color:#444;text-align:justify}
.slide--tech .page-no{color:rgba(255,255,255,.7)}
</style>
</head>
<body>

<section class="slide slide--cover">
  <div class="cover-photo" role="img" aria-label="Aerial photo of a coastal city skyline beside the sea, tinted blue"></div>
  <div class="cover-frame"></div>
  <div class="cover-panel"></div>
  <div class="cover-dot"></div>
  <h1 class="cover-title">Amber Heron Fund</h1>
  <p class="footer-note">Not for distribution – All rights reserved © Amber Heron Fund</p>
  <p class="page-no">page | 1</p>
</section>

<section class="slide slide--contents">
  <div class="contents-side" role="img" aria-label="Faceted low-poly texture in dark slate blue"></div>
  <h2 class="contents-heading">TABLE<br><strong>CONTENT</strong></h2>
  <div class="contents-frame"></div>
  <ol class="contents-list">
    <li><span class="num">01</span>The Edge</li>
    <li><span class="num">02</span>The Technology</li>
    <li><span class="num">03</span>The People</li>
    <li><span class="num">04</span>The Market</li>
    <li><span class="num">05</span>Our Process</li>
    <li><span class="num">06</span>Our Customers</li>
    <li><span class="num">07</span>Advantage:</li>
    <li><span class="num">08</span>Management Structure</li>
    <li><span class="num">09</span>Crossroads</li>
    <li><span class="num">10</span>Projected Size of Fund</li>
  </ol>
  <span class="brand-mark">Amber Heron</span>
  <p class="footer-note">Not for distribution – All rights reserved © Amber Heron Fund</p>
  <p class="page-no">page | 2</p>
</section>

<section class="slide slide--edge">
  <svg class="diagonal" viewBox="0 0 818 460" role="img" aria-label="Dark blue tinted photo of a laptop keyboard">
    <defs>
      <linearGradient id="edgeFill" x1="0" y1="0" x2="0" y2="1">
        <stop offset="0" stop-color="#1e3a7a"/>
        <stop offset="1" stop-color="#12275a"/>
      </linearGradient>
    </defs>
    <polygon points="377,0 818,0 818,460 106,460" fill="url(#edgeFill)"/>
  </svg>
  <div class="section-card">
    <span class="section-num">01</span>
    <h2 class="section-title">The Edge</h2>
  </div>
  <div class="edge-copy">
    <p>Experience with fund management and asset disposal. Utilizing the clues and hints that borrowers and guarantors leave on the Internet, we can special service assets and collect on them more quickly and maximize return.</p>
    <p>Much of the technology and experience as a team can be attributed to the team’s experience at Cedarleaf. The principals were the management team that came on in March 2020 and grew the business from less than 12,000 PPP loans to more than 800,000.</p>
  </div>
  <span class="brand-mark">Amber Heron</span>
  <p class="footer-note">Not for distribution – All rights reserved © Amber Heron Fund</p>
  <p class="page-no">page | 3</p>
</section>

<section class="slide slide--tech">
  <svg class="diagonal" viewBox="0 0 818 460" role="img" aria-label="Faceted low-poly texture in slate blue fading to near black">
    <defs>
      <linearGradient id="techFill" x1="0" y1="0" x2="0" y2="1">
        <stop offset="0" stop-color="#5a6fa3"/>
        <stop offset=".5" stop-color="#343f63"/>
        <stop offset="1" stop-color="#181b26"/>
      </linearGradient>
    </defs>
    <polygon points="626,0 818,0 818,460 354,460" fill="url(#techFill)"/>
  </svg>
  <div class="tech-copy">
    Most lenders and servicers use LedgerCore or ServPath and then software like CollectPro for collections.
    These software packages fail to address the most important factors which is to analyze the borrower (and the guarantors) to allow for customized collection plans. We use enhanced skip tracing developed during PPP forgiveness and collection efforts with advanced social media logic.
    Finally, we use evolving algorithms to price and purchase NPL portfolios at the correct price.
    We offer a product that can allow our users to save more money and earn passive income.
  </div>
  <div class="section-card">
    <span class="section-num">02</span>
    <h2 class="section-title">The Technology</h2>
  </div>
  <span class="brand-mark">Amber Heron</span>
  <p class="footer-note">Not for distribution – All rights reserved © Amber Heron Fund</p>
  <p class="page-no">page | 4</p>
</section>

</body>
</html>
```